Service company standing banner design

We are an existing company that just updated our logo. We are attending some oportunity summits in the near future and want a new crisp clean look on our three banners that will be placed in the back of our small booth. The summits we are attending are designed to give local companies opportunities on a prokect we have been awarded to construct in their area. These banners should communicate who we are with no questions when people see them. One banner shall list our services. One to list our values and one to state our goals. All these while being appealing to the eye and using picture of nature. Attached are copies of what we are to replace. also the new logo and the original background pictures in the existing banners

```html
<!DOCTYPE html>
<html lang="en">
<head>
<meta charset="utf-8">
<title>Norvale Services – Booth Banners</title>
<link href="https://fonts.googleapis.com/css2?family=Montserrat:wght@800&family=Nunito:wght@800&display=swap" rel="stylesheet">
<style>
  :root {
    --paper: #ffffff;
    --ink-light: #ffffff;
    --brand-blue: #1f3fa3;
    --brand-orange: #f07d1a;
    --forest-dark: #1f2a22;
    --forest-mid: #3a4a38;
    --river-teal: #4f8f8f;
    --sky-slate: #5d6f8c;
    --snow: #eef1f5;
    --mountain-green: #3f5540;
    --glacier: #8fc5c6;
  }
  * { margin: 0; padding: 0; box-sizing: border-box; }
  html, body { width: 1200px; height: 904px; overflow: hidden; background: var(--paper); }
  .canvas { position: relative; width: 1200px; height: 904px; background: var(--paper); }

  .banner {
    position: absolute; top: 20px; width: 371px; height: 863px;
    overflow: hidden; color: var(--ink-light);
  }
  .banner--values { left: 23px; }
  .banner--services { left: 415px; }
  .banner--goals { left: 810px; }

  .banner__photo { position: absolute; inset: 0; }
  .banner--values .banner__photo {
    background: linear-gradient(180deg, var(--forest-dark) 0%, var(--forest-mid) 40%, var(--river-teal) 60%, #6a6a4a 85%, #8a8458 100%);
  }
  .banner--services .banner__photo {
    background: linear-gradient(180deg, #4b5d7c 0%, var(--sky-slate) 35%, #aab4c2 58%, #d7dde5 72%, var(--snow) 100%);
  }
  .banner--goals .banner__photo {
    background: linear-gradient(180deg, #6c7a6e 0%, var(--mountain-green) 25%, #2f4530 52%, #7d8a76 62%, var(--glacier) 75%, #9aa7a3 90%, #b7aa98 100%);
  }

  /* Values */
  .values {
    position: absolute; left: 40px; top: 112px; width: 290px;
    font-family: "Montserrat", sans-serif; font-weight: 800;
    text-align: center; line-height: 1;
  }
  .values__rule { height: 6px; background: var(--ink-light); }
  .values__word { display: block; letter-spacing: 0.5px; }
  .values__word--integrity { font-size: 46px; margin-top: 22px; }
  .values__word--transparency { font-size: 30px; margin-top: 14px; }
  .values__word--respect { font-size: 57px; margin-top: 14px; }
  .values__word--trust { font-size: 78px; margin-top: 8px; margin-bottom: 14px; }

  /* Services */
  .services {
    position: absolute; left: 39px; top: 100px;
    font-family: "Nunito", sans-serif; font-weight: 800;
    font-size: 27px; line-height: 38.5px; list-style: none;
  }
  .services__frame { position: absolute; left: 0; top: 0; }

  /* Goals */
  .mission-frame { position: absolute; left: 35px; top: 108px; }
  .mission-frame__text {
    position: absolute; left: 35px; top: 96px; width: 300px; text-align: center;
    font-family: "Nunito", sans-serif; font-weight: 800;
    font-size: 26px; line-height: 50px;
  }
  .mission-frame__text span { display: block; line-height: 32px; }
  .mission-frame__lead { font-size: 27px; margin-bottom: 14px; }
  .goal-statement {
    position: absolute; left: 10px; top: 245px; width: 351px; text-align: center;
    font-family: "Nunito", sans-serif; font-weight: 800;
    font-size: 27px; line-height: 38.5px;
  }

  /* Brand plate */
  .brand-plate {
    position: absolute; left: 25px; top: 714px; width: 321px; height: 101px;
    background: var(--paper); border-radius: 22px;
    display: flex; align-items: center; gap: 12px; padding: 0 16px;
  }
  .brand-plate__dot { width: 46px; height: 46px; border-radius: 50%; background: var(--brand-orange); flex: none; }
  .brand-plate__name {
    font-family: "Nunito", sans-serif; font-weight: 800; color: var(--brand-blue);
    font-size: 24px; line-height: 26px;
  }
  .brand-plate__name span { display: block; }
</style>
</head>
<body>
<main class="canvas">

  <section class="banner banner--values">
    <div class="banner__photo" role="img" aria-label="Evergreen forest above a teal river bending past a grassy rocky bluff"></div>
    <div class="values">
      <div class="values__rule"></div>
      <span class="values__word values__word--integrity">INTEGRITY</span>
      <span class="values__word values__word--transparency">TRANSPARENCY</span>
      <span class="values__word values__word--respect">RESPECT</span>
      <span class="values__word values__word--trust">TRUST</span>
      <div class="values__rule"></div>
    </div>
    <div class="brand-plate">
      <div class="brand-plate__dot"></div>
      <div class="brand-plate__name"><span>Norvale Services</span><span>Limited Partnership</span></div>
    </div>
  </section>

  <section class="banner banner--services">
    <div class="banner__photo" role="img" aria-label="Snow-covered spruce trees and a snowy clearing under a grey-blue cloudy sky"></div>
    <svg class="services__frame" width="371" height="440" aria-hidden="true">
      <path d="M330 142 V425 H39" fill="none" stroke="#ffffff" stroke-width="6"/>
    </svg>
    <ul class="services">
      <li>Pipeline construction</li>
      <li>Pipeline Clearing</li>
      <li>Land Clearing</li>
      <li>Civil Works</li>
      <li>Road Maintenenece</li>
      <li>Reclamation</li>
      <li>Logging</li>
      <li>Mulching</li>
    </ul>
    <div class="brand-plate">
      <div class="brand-plate__dot"></div>
      <div class="brand-plate__name"><span>Norvale Services</span><span>Limited Partnership</span></div>
    </div>
  </section>

  <section class="banner banner--goals">
    <div class="banner__photo" role="img" aria-label="Mountain slope with tall evergreens above a rushing glacial river and driftwood"></div>
    <svg class="mission-frame" width="300" height="124" aria-hidden="true">
      <path d="M82 3 H3 V121 H297 V3 H262" fill="none" stroke="#ffffff" stroke-width="6"/>
    </svg>
    <div class="mission-frame__text">
      <span class="mission-frame__lead">HONOURING</span>
      <span>the interests of</span>
      <span>Indigenous people</span>
    </div>
    <p class="goal-statement">To build and grow a strong regional business providing the best quality for our people and clients</p>
    <div class="brand-plate">
      <div class="brand-plate__dot"></div>
      <div class="brand-plate__name"><span>Norvale Services</span><span>Limited Partnership</span></div>
    </div>
  </section>

</main>
</body>
</html>
```